Cafe menu flyer design

I need if possible A4 double sided menus. Two exemplars: first will contain breakfast menu on one side & refreshments menu on the other side, second exemplar will contain lunch menu on one side & refreshments menu on the other side. We do not need a description of the cafe or any history on these flyers, but design should reflect our surroundings and activities this area. We are located in main ski resort in UK-Cairngorm Mountains, right on the main ski road. The slopes are only 2 miles away from us. We are also very popular with wild life enthusiasts. Continues in design brief!

```html
<!DOCTYPE html>
<html lang="en">
<head>
<meta charset="utf-8">
<title>Mara's @ Pinewood Cafe – Menu</title>
<link rel="stylesheet" href="https://fonts.googleapis.com/css2?family=Carlito:ital,wght@0,400;0,700;1,400;1,700&family=Gelasio:ital@1&display=swap">
<style>
:root{
  --page-bg:#8ea4a2;
  --navy:#24358a;
  --ink:#1e2736;
  --sky-top:#c6d1e6;
  --sky-mid:#eef1f7;
  --snow:#f6f7fa;
  --rock:#b6bfcc;
  --note-panel:rgba(150,165,205,.55);
  --pancake:#d79a4c;
  --plate:#eef0f4;
}
*{margin:0;padding:0;box-sizing:border-box}
html,body{width:1200px;height:960px;overflow:hidden}
body{background:var(--page-bg);font-family:"Carlito",Calibri,sans-serif;color:var(--ink)}
.flyer{position:absolute;left:280px;top:30px;width:640px;height:900px;
  background:linear-gradient(180deg,var(--sky-top) 0%,var(--sky-mid) 22%,var(--snow) 60%,#eef0f5 100%);
  box-shadow:0 10px 30px rgba(0,0,0,.25);overflow:hidden}
.mountain-scene{position:absolute;left:0;top:320px;width:640px;height:470px;
  background:radial-gradient(ellipse at 60% 55%,var(--rock) 0%,rgba(200,208,220,.7) 35%,rgba(240,242,247,0) 70%),
             linear-gradient(180deg,rgba(220,226,236,.6),rgba(246,247,250,.2))}
.cafe-name{position:absolute;top:34px;width:100%;text-align:center;font-size:31px;font-weight:700;color:var(--navy)}
.section-title{position:absolute;top:100px;font-size:17px;font-weight:700;color:var(--navy)}
.section-rule{position:absolute;top:130px;height:2px;background:var(--navy)}
.column-divider{position:absolute;left:321px;top:120px;width:2px;height:712px;background:var(--navy)}
.menu-column{position:absolute;display:flex;flex-direction:column}
.menu-breakfast{left:12px;top:147px;width:300px}
.menu-refreshments{left:326px;top:151px;width:288px}
.item{position:relative;font-size:12.2px;line-height:14.5px;margin-bottom:10.5px;white-space:nowrap}
.item .price{position:absolute;right:0;bottom:0;text-align:right;white-space:nowrap}
.note{font-size:12px;line-height:13.5px;font-style:italic;margin-bottom:10.5px}
.note-strong{font-weight:700;color:var(--navy)}
.notes-panel{position:absolute;left:0;top:596px;width:320px;height:64px;background:var(--note-panel)}
.panel-note{position:absolute;left:12px;top:601px;width:300px}
.pancake-photo{position:absolute;left:0;top:660px;width:320px;height:172px;
  background:radial-gradient(ellipse at 55% 55%,var(--pancake) 0%,#c47f34 35%,var(--plate) 62%,#dfe3ea 100%)}
.footer-rule{position:absolute;left:0;top:834px;width:640px;height:2px;background:var(--navy)}
.footer{position:absolute;top:842px;width:100%;text-align:center;font-family:"Gelasio",Georgia,serif;font-style:italic;font-size:11.5px;line-height:16px;color:var(--navy)}
</style>
</head>
<body>
<main class="flyer">
  <div class="mountain-scene" role="img" aria-label="Snow-covered mountain peaks behind the menu"></div>

  <h1 class="cafe-name">Mara’s @ Pinewood Cafe</h1>

  <h2 class="section-title" style="left:12px">Breakfast 9am - 12noon</h2>
  <div class="section-rule" style="left:12px;width:300px"></div>
  <h2 class="section-title" style="left:326px">Refreshments</h2>
  <div class="section-rule" style="left:326px;width:282px"></div>
  <div class="column-divider"></div>

  <section class="menu-column menu-breakfast">
    <div class="item"><span>Small breakfast (bacon, egg, sausage)</span><span class="price">£5.50</span></div>
    <div class="item"><span>Large breakfast ( bacon, egg, sausage, black pudding,<br>potato scone, beans, tomato)</span><span class="price">£7.95</span></div>
    <p class="note">Both breakfast include tea/coffe/plain hot chocolate &amp;<br>one slice of toast. One free refill drink</p>
    <div class="item"><span>Pancake breakfast. Three pancakes served with hot<br>forest berry sauce and maple syrup<br>Add three rushers of bacon</span><span class="price">£4.95<br>£6.95</span></div>
    <div class="item"><span>Round of toast,served with butter and jam</span><span class="price">£2.00</span></div>
    <div class="item"><span>Beans on toast</span><span class="price">£3.50</span></div>
    <div class="item"><span>Beans &amp; egg on toast</span><span class="price">£4.00</span></div>
    <div class="item"><span>Beans &amp; bacon on toast</span><span class="price">£4.50</span></div>
    <div class="item"><span>Bacon roll</span><span class="price">£2.90</span></div>
    <div class="item"><span>Lorne roll</span><span class="price">£2.50</span></div>
    <div class="item"><span>Black pudding roll</span><span class="price">£2.50</span></div>
    <div class="item"><span>Fried egg roll<br>2 item roll</span><span class="price">£2.00<br>£4.00</span></div>
    <div class="item"><span>Rolls with assorted cold fillings</span><span class="price">£2.20 - £3.20</span></div>
    <div class="item"><span>Pies assorted</span><span class="price">£2.50</span></div>
  </section>

  <div class="notes-panel"></div>
  <p class="note note-strong panel-note">Gluten free bread, cakes and veggie breakfast available<br>- ask staff!<br>At the hight of the season evening meals available.<br>Ask staff for more information.</p>
  <div class="pancake-photo" role="img" aria-label="Stack of pancakes with maple syrup on a plate"></div>

  <section class="menu-column menu-refreshments">
    <div class="item"><span>Tea</span><span class="price">£1.50</span></div>
    <div class="item"><span>Filter Coffee, decaf coffee, plain hot chocolate</span><span class="price">£2.00</span></div>
    <div class="item"><span>Selection of herbal teas</span><span class="price">£2.00</span></div>
    <div class="item"><span>Specialty strawberry, raspberry, apple &amp; mint tea( black<br>tea with your choice of syrup)</span><span class="price">£2.50</span></div>
    <div class="item"><span>Assorted premium “Leaf House” teas</span><span class="price">£2.50</span></div>
    <div class="item"><span>Hot chocolate with cream</span><span class="price">£2.20</span></div>
    <div class="item"><span>Hot chocolate with marsh mallows</span><span class="price">£2.20</span></div>
    <div class="item"><span>Hot chocolate with cream &amp; marsh mallows</span><span class="price">£2.20</span></div>
    <div class="item"><span>Hot chocolate with brandy</span><span class="price">£3.50</span></div>
    <div class="item"><span>Hot chocolate with brandy,<br>marsh mallows &amp; cream</span><span class="price">£4.50</span></div>
    <div class="item"><span>Cafe Latte/Cappucino</span><span class="price">£2.50</span></div>
    <div class="item"><span>Squirrel Latte</span><span class="price">£3.50</span></div>
    <div class="item"><span>Chocolate Latte</span><span class="price">£3.50</span></div>
    <div class="item"><span>Cinnamon Latte</span><span class="price">£3.50</span></div>
    <div class="item"><span>Caramel Latte</span><span class="price">£3.50</span></div>
    <div class="item"><span>Butterscotch Latte</span><span class="price">£3.50</span></div>
    <div class="item"><span>Gingerbread Latte</span><span class="price">£3.50</span></div>
    <div class="item"><span>Mocha</span><span class="price">£3.50</span></div>
    <div class="item"><span>Glass of milk</span><span class="price">£1.20</span></div>
    <div class="item"><span>Milkshakes</span><span class="price">£2.00</span></div>
    <div class="item"><span>Still or Sparkling water</span><span class="price">£1.80</span></div>
    <div class="item"><span>Cans of juice</span><span class="price">£1.60</span></div>
    <div class="item"><span>Cartons of juice</span><span class="price">£1.30</span></div>
    <p class="note note-strong">We use semi skimmed milk only</p>
    <p class="note note-strong">At the hight of the season evening meals available. Ask<br>staff for more information.</p>
  </section>

  <div class="footer-rule"></div>
  <footer class="footer">
    Mara’s @ Pinewood Cafe, Pinewood, Strathbeg, PH99 9ZZ. Tel:01000 555123<br>
    Find us online
  </footer>
</main>
</body>
</html>
```